Original and Visually striking Realtor Business Card

I'm a real estate agent in the Richmond (VA) area. I'd like something that stands out from the cliche realtor business card. I want it to look nice.

My two taglines are as follows and you can use either or both... perhaps one on the front, one on the back. Whatever looks best.

1. Upbeat. Warm. Here for YOU.
and
2. YOU are the most important person.

Thank you for your input.
Updates

Your designs and creativity are great so far. I just found out from my supervising broker that I need to include 2 small realtor logos (the one with the R - KPT and the Equal Housing one.) They can be quite small. I added a few other pictures to choose from too. Thank you all for your excellent work.

Target Market(s)

home buyers and home sellers

Industry/Entity Type

Real Estate

Contact Information for Business Card

Lorna Vatch, Sales Agent
Upbeat. Warm. Here for YOU.
Coltrane Realtors OVK®
20417 E Maple Ave #300, Glen Allen, VA 23060
www.findyourdoorstep.example
lorna.vatch@mailbox.example
(804) 555-0142 office
(804) 555-0187 cell

Requirements
Must have
• Ok.. so I definitely need a picture of myself and I've included a few to choose from. And my company logo. I would like my picture to be the central image, larger than the company logo. The other pictures are some recognizable landmarks in Richmond (not necessary, but just wanted you to have some choices)

I need to have the realtor logo (R) with the KPT as well as the Equal Housing logo (they can be small.)

Double sided please

Should not have
• nothing cheesy or too cliche please

```html
<!DOCTYPE html>
<html lang="en">
<head>
<meta charset="utf-8">
<title>Lorna Vatch, Sales Agent – Business Card</title>
<link rel="stylesheet" href="https://fonts.googleapis.com/css2?family=Oswald:wght@300;400;700&display=swap">
<style>
  :root {
    --paper: #ffffff;
    --ink: #1c1c1c;
    --brand: #8a1538;
    --brand-mark: #c8102e;
    --portrait-light: #8c8c8c;
    --portrait-dark: #2e2e2e;
  }
  html, body {
    margin: 0;
    padding: 0;
    overflow: hidden;
    background: var(--paper);
  }
  .card {
    position: relative;
    width: 1200px;
    height: 702px;
    background: var(--paper);
    overflow: hidden;
    font-family: "Oswald", "Arial Narrow", sans-serif;
  }
  .agent-name {
    position: absolute;
    left: 46px;
    top: 34px;
    margin: 0;
    font-weight: 700;
    font-size: 64px;
    line-height: 1.1;
    letter-spacing: -0.5px;
    color: var(--ink);
    white-space: nowrap;
  }
  .company-mark {
    position: absolute;
    left: 47px;
    top: 250px;
    display: flex;
    align-items: center;
    gap: 14px;
  }
  .company-mark .mark-square {
    width: 46px;
    height: 46px;
    background: var(--brand-mark);
  }
  .company-mark .mark-name {
    font-weight: 700;
    font-size: 58px;
    line-height: 1;
    color: var(--brand-mark);
  }
  .contact {
    position: absolute;
    left: 46px;
    top: 396px;
    margin: 0;
    font-style: normal;
    font-weight: 300;
    font-size: 24px;
    line-height: 33px;
    color: var(--brand);
  }
  .contact span { display: block; white-space: nowrap; }
  .tagline {
    position: absolute;
    left: 46px;
    top: 584px;
    margin: 0;
    font-weight: 300;
    font-size: 54px;
    line-height: 1.1;
    color: var(--ink);
    white-space: nowrap;
  }
  .tagline .dot { margin: 0 10px; }
  .tagline strong { font-weight: 700; }
  .portrait {
    position: absolute;
    left: 711px;
    top: 22px;
    width: 471px;
    height: 662px;
    background: linear-gradient(150deg, var(--portrait-light) 0%, #5a5a5a 55%, var(--portrait-dark) 100%);
  }
</style>
</head>
<body>
  <div class="card">
    <h1 class="agent-name">Lorna Vatch, Sales Agent</h1>

    <div class="company-mark">
      <div class="mark-square"></div>
      <div class="mark-name">OVK</div>
    </div>

    <address class="contact">
      <span>Coltrane Realtors OVK®</span>
      <span>20417 E Maple Ave #300, Glen Allen, VA 23060</span>
      <span>www.findyourdoorstep.example lorna.vatch@mailbox.example</span>
      <span>(804) 555-0142 office</span>
      <span>(804) 555-0187 cell</span>
    </address>

    <p class="tagline">Upbeat<span class="dot">•</span>Warm<span class="dot">•</span>Here for <strong>YOU</strong></p>

    <div class="portrait" role="img" aria-label="Black and white portrait photo of the agent, smiling"></div>
  </div>
</body>
</html>
```